Evaporative Air Conditioning Summer Service

Would like to design a flyer to send out in an email to existing clients to promote a Pre-summer service for Evaporative Air Conditioners
Cost will be $110.00 inc gst
Tasks included in service are
- Inspection and clean of pads
- Inspection and check float valve, water pump, fan, motor, bearings, drain
- Clean basin
- Supply of bacterial tablet
- Inspect overall condition of unit
- Any repairs if required will be quoted
Please see files attached of a previous very basic flyer I have used for installation and replacement unit costs. This has current contact information
Have also uploaded company logo for use.
Thanks

```html
<!DOCTYPE html>
<html lang="en">
<head>
<meta charset="utf-8">
<title>Pre-Summer Evaporative Air Conditioner Service – Harbourline Gas &amp; Plumbing</title>
<link rel="stylesheet" href="https://fonts.googleapis.com/css2?family=Poppins:wght@500;600;700&family=Lexend:wght@300;400&display=swap">
<style>
  :root {
    --orange: #ff7a00;
    --orange-deep: #fc7400;
    --yellow: #f3d31c;
    --blue-deep: #2353a6;
    --blue-mid: #1b72b5;
    --blue-bright: #0ea5dc;
    --white: #ffffff;
    --unit-light: #eef1f4;
    --unit-shade: #c9d3dc;
  }
  * { margin: 0; padding: 0; box-sizing: border-box; }
  html, body { width: 927px; height: 1200px; overflow: hidden; background: var(--white); }
  .flyer {
    position: relative;
    width: 927px;
    height: 1200px;
    overflow: hidden;
    background: var(--white);
    font-family: "Poppins", sans-serif;
  }

  /* Brand */
  .brand {
    position: absolute;
    top: 58px;
    left: 0;
    width: 927px;
    display: flex;
    justify-content: center;
    align-items: center;
    gap: 14px;
  }
  .brand-dot {
    width: 58px; height: 58px;
    border-radius: 50%;
    background: var(--orange);
  }
  .brand-name {
    font-family: "Poppins", sans-serif;
    font-weight: 700;
    color: var(--blue-deep);
    font-size: 30px;
    line-height: 1.05;
    letter-spacing: 0.5px;
  }
  .brand-name span { display: block; font-size: 15px; letter-spacing: 2px; }

  /* Title banner */
  .title-band {
    position: absolute;
    top: 151px; left: 0;
    width: 927px; height: 81px;
    background: linear-gradient(90deg, var(--yellow) 0%, var(--orange) 12%, var(--orange) 82%, var(--yellow) 100%);
    display: flex; align-items: center; justify-content: center;
  }
  .title-band h1 {
    color: var(--white);
    font-weight: 700;
    font-size: 26px;
    letter-spacing: 0.6px;
    white-space: nowrap;
  }

  /* Hero */
  .hero { position: absolute; top: 242px; left: 0; width: 927px; height: 444px; }
  .hero svg { position: absolute; inset: 0; }
  .hero-product {
    position: absolute;
    top: -18px; left: 290px;
    width: 612px; height: 412px;
    border-radius: 18px;
    background: linear-gradient(160deg, var(--white) 0%, var(--unit-light) 55%, var(--unit-shade) 100%);
  }

  /* Price panel */
  .price-panel { position: absolute; top: 694px; left: 0; width: 336px; height: 305px; }
  .price-panel svg { position: absolute; inset: 0; }
  .price {
    position: absolute;
    left: 0; width: 274px; top: 100px;
    text-align: center;
    color: var(--white);
  }
  .price strong { display: block; font-size: 46px; font-weight: 700; line-height: 1; }
  .price span { display: block; font-size: 24px; font-weight: 600; margin-top: 4px; }

  /* Service list */
  .services { position: absolute; left: 347px; top: 694px; width: 580px; list-style: none; }
  .services li {
    display: flex; align-items: center;
    margin-bottom: 9px;
    height: 52px;
    padding-left: 10px;
    border-radius: 22px 0 0 22px;
    color: var(--white);
    font-family: "Lexend", sans-serif;
    font-weight: 300;
    font-size: 23px;
    line-height: 1.05;
    letter-spacing: 0.4px;
    white-space: nowrap;
  }
  .services li:nth-child(odd)  { background: linear-gradient(90deg, var(--orange-deep) 0%, var(--orange) 55%, var(--yellow) 85%); }
  .services li:nth-child(even) { background: linear-gradient(90deg, var(--orange-deep) 0%, var(--orange) 70%, var(--yellow) 100%); }
  .services li.tall { height: 62px; }
  .sparkle { width: 28px; height: 28px; flex: none; margin-right: 8px; }
  .sparkle path { fill: currentColor; }

  .note {
    position: absolute; left: 357px; top: 1005px;
    display: flex; align-items: center;
    color: var(--blue-mid);
    font-family: "Lexend", sans-serif;
    font-weight: 400;
    font-size: 22.5px;
    letter-spacing: 0.5px;
    white-space: nowrap;
  }

  /* Footer */
  .contact {
    position: absolute; top: 1070px; left: 0;
    width: 927px; height: 130px;
    background: var(--blue-mid);
    color: var(--white);
  }
  .contact h2 {
    position: absolute; left: 65px; top: 46px;
    font-size: 29px; font-weight: 600; letter-spacing: 1.2px;
  }
  .contact-badge {
    position: absolute; left: 312px; top: 16px;
    width: 98px; height: 98px; border-radius: 50%;
    background: var(--white);
  }
  .contact-details {
    position: absolute; left: 444px; top: 30px;
    list-style: none;
    font-size: 18.5px; font-weight: 600; line-height: 25px; letter-spacing: 0.5px;
  }
</style>
</head>
<body>
<main class="flyer">

  <header class="brand">
    <div class="brand-dot"></div>
    <div class="brand-name">HARBOURLINE<span>GAS &amp; PLUMBING</span></div>
  </header>

  <div class="title-band">
    <h1>PRE-SUMMER SERVICE FOR EVAPORATIVE AIR CONDITIONERS</h1>
  </div>

  <section class="hero">
    <svg width="927" height="444" viewBox="0 0 927 444" aria-hidden="true">
      <defs>
        <linearGradient id="heroBlue" x1="0" y1="0" x2="1" y2="1">
          <stop offset="0" stop-color="#2353a6"/>
          <stop offset="0.5" stop-color="#0ea5dc"/>
          <stop offset="1" stop-color="#2353a6"/>
        </linearGradient>
      </defs>
      <path d="M0,0 H600 L700,60 C790,130 880,220 927,330 V444 H275 C160,370 40,240 0,110 Z" fill="url(#heroBlue)"/>
    </svg>
    <div class="hero-product" role="img" aria-label="White split-system air conditioner with outdoor unit and indoor wall unit, with sparkles and airflow swooshes"></div>
  </section>

  <aside class="price-panel">
    <svg width="336" height="305" viewBox="0 0 336 305" aria-hidden="true">
      <path d="M0,0 H316 Q336,0 336,20 V285 Q336,305 316,305 H0 Z" fill="#f3d31c"/>
      <path d="M0,0 H326 L273,149 L326,305 H0 Z" fill="#ff7a00"/>
    </svg>
    <p class="price"><strong>$110.00</strong><span>inc gst</span></p>
  </aside>

  <ul class="services">
    <li><svg class="sparkle" viewBox="0 0 28 28"><path d="M14 0 C15 10 18 13 28 14 C18 15 15 18 14 28 C13 18 10 15 0 14 C10 13 13 10 14 0Z"/></svg>Inspection and clean of pads</li>
    <li class="tall"><svg class="sparkle" viewBox="0 0 28 28"><path d="M14 0 C15 10 18 13 28 14 C18 15 15 18 14 28 C13 18 10 15 0 14 C10 13 13 10 14 0Z"/></svg>Inspection and check float valve,<br>waterpump, fan, motor, bearings, drain</li>
    <li><svg class="sparkle" viewBox="0 0 28 28"><path d="M14 0 C15 10 18 13 28 14 C18 15 15 18 14 28 C13 18 10 15 0 14 C10 13 13 10 14 0Z"/></svg>Clean basin</li>
    <li><svg class="sparkle" viewBox="0 0 28 28"><path d="M14 0 C15 10 18 13 28 14 C18 15 15 18 14 28 C13 18 10 15 0 14 C10 13 13 10 14 0Z"/></svg>Supply of bacterial tablet</li>
    <li><svg class="sparkle" viewBox="0 0 28 28"><path d="M14 0 C15 10 18 13 28 14 C18 15 15 18 14 28 C13 18 10 15 0 14 C10 13 13 10 14 0Z"/></svg>Inspect overall condition of unit</li>
  </ul>

  <p class="note"><svg class="sparkle" viewBox="0 0 28 28"><path d="M14 0 C15 10 18 13 28 14 C18 15 15 18 14 28 C13 18 10 15 0 14 C10 13 13 10 14 0Z"/></svg>Any repairs if required will be quoted</p>

  <footer class="contact">
    <h2>CONTACT US</h2>
    <div class="contact-badge"></div>
    <ul class="contact-details">
      <li>0491570156</li>
      <li>admin@harbourlinegasplumbing.com.au</li>
      <li>ABN 12345678901</li>
    </ul>
  </footer>

</main>
</body>
</html>
```